Bellweather Business Card & Letterhead
Business Card & Letterhead Design
I need single sided standard sized Business Card [3.5" x 2"]
Use whatever font you think looks best
Simple
Lorena Fitchett
71 Pellham Lane
Marietta, Georgia 30008
lorena@bellweatherpartners.example
www.bellweatherpartners.example

```html
<!DOCTYPE html>
<html lang="en">
<head>
<meta charset="utf-8">
<title>Bellweather Stationery Concepts</title>
<link href="https://fonts.googleapis.com/css2?family=Lato:wght@400;700;900&family=Lora:wght@400&display=swap" rel="stylesheet">
<style>
  :root{
    --board-dark:#2b2b2b;
    --board-light:#5a5a5a;
    --paper:#ffffff;
    --paper-shade:#ececec;
    --brand-blue:#1f6fbd;
    --flap-grey:#8e8e8e;
    --ink:#3a3a3a;
    --muted:#9a9a9a;
    --label:#cfcfcf;
  }
  *{margin:0;padding:0;box-sizing:border-box}
  html,body{width:1200px;height:569px;overflow:hidden}
  body{
    position:relative;
    font-family:"Lato",sans-serif;
    background:radial-gradient(ellipse at 55% 35%,var(--board-light) 0%,var(--board-dark) 75%);
  }
  .sheet{position:absolute;background:var(--paper);box-shadow:0 3px 10px rgba(0,0,0,.45)}
  .brand{display:flex;align-items:center;gap:6px;color:var(--brand-blue);font-weight:900;letter-spacing:.3px;white-space:nowrap}
  .brand-mark{background:var(--brand-blue);display:inline-block;flex:none}
  .caption{position:absolute;color:var(--label);font-size:9px;text-align:center}

  /* board title */
  .board-title{position:absolute;left:42px;top:190px;width:220px}
  .board-title .brand{color:#fff;font-size:22px;gap:8px}
  .board-title .brand-mark{background:#fff;width:26px;height:26px;border-radius:3px}
  .board-subtitle{margin:6px 0 0 34px;font-family:"Lora",serif;color:#e6e6e6;font-size:14px}

  /* business card */
  .card{left:36px;top:281px;width:223px;height:122px;overflow:hidden}
  .card .brand{position:absolute;left:28px;top:20px;font-size:17px}
  .card .brand-mark{width:19px;height:19px}
  .card-band{position:absolute;left:0;bottom:0;width:100%;height:60px;background:var(--brand-blue);color:#fff;display:flex;padding:9px 10px;gap:8px}
  .card-person{width:86px;font-size:7px;line-height:1.4;white-space:nowrap}
  .card-person strong{display:block;font-size:8px}
  .card-contact{font-size:5.5px;line-height:1.6;white-space:nowrap}

  /* letterhead */
  .letterhead{left:276px;top:36px;width:379px;height:480px}
  .letterhead .brand{position:absolute;left:0;right:0;top:22px;justify-content:center;font-size:16px}
  .letterhead .brand-mark{width:18px;height:18px}
  .sheet-footer{position:absolute;left:0;bottom:0;width:100%;height:12px;background:var(--brand-blue);color:#fff;font-size:6px;line-height:12px;text-align:center}

  /* envelopes */
  .envelope{overflow:hidden}
  .envelope svg{position:absolute;left:0;top:0}
  .envelope .brand-mark.flap-mark{position:absolute;width:24px;height:24px;background:var(--brand-blue);border:2px solid #fff}
  .env-web{position:absolute;width:100%;text-align:center;font-size:5.5px;color:var(--muted)}
  .env-back-grey{left:713px;top:36px;width:475px;height:144px}
  .env-back-blue{left:761px;top:132px;width:439px;height:156px}
  .env-back-white{left:713px;top:240px;width:475px;height:144px}
  .env-front{left:679px;top:348px;width:480px;height:168px}
  .env-front .brand{position:absolute;left:16px;top:14px;font-size:14px}
  .env-front .brand-mark{width:16px;height:16px}
  .env-return{position:absolute;left:16px;top:38px;font-size:5.5px;color:var(--ink)}
</style>
</head>
<body>

  <div class="board-title">
    <div class="brand"><span class="brand-mark"></span>BELLWEATHER</div>
    <p class="board-subtitle">Stationary Concepts</p>
  </div>

  <div class="sheet card">
    <div class="brand"><span class="brand-mark"></span>BELLWEATHER</div>
    <div class="card-band">
      <div class="card-person"><strong>Lorena Fitchett</strong>Principal Broker<br>71 Pellham Lane<br>Marietta, Georgia 30008</div>
      <div class="card-contact">T 770 555 0148<br>lorena@bellweatherpartners.example<br>www.bellweatherpartners.example<br>lbfitchett</div>
    </div>
  </div>
  <p class="caption" style="left:36px;top:412px;width:223px">Front Card</p>

  <div class="sheet letterhead">
    <div class="brand"><span class="brand-mark"></span>BELLWEATHER</div>
    <div class="sheet-footer">www.bellweatherpartners.example</div>
  </div>
  <p class="caption" style="left:276px;top:530px;width:379px">Letterhead design A4</p>

  <div class="sheet envelope env-back-grey">
    <svg width="475" height="144" viewBox="0 0 475 144">
      <polyline points="0,144 237,70 475,144" fill="none" stroke="var(--paper-shade)" stroke-width="1.5"/>
      <polygon points="0,0 475,0 475,25 237,68 0,25" fill="var(--flap-grey)"/>
    </svg>
    <span class="brand-mark flap-mark" style="left:225px;top:26px"></span>
    <p class="env-web" style="top:74px">www.bellweatherpartners.example</p>
  </div>

  <div class="sheet envelope env-back-blue">
    <svg width="439" height="156" viewBox="0 0 439 156">
      <polyline points="0,156 219,80 439,156" fill="none" stroke="var(--paper-shade)" stroke-width="1.5"/>
      <polygon points="0,0 439,0 439,28 219,76 0,28" fill="var(--brand-blue)"/>
    </svg>
    <span class="brand-mark flap-mark" style="left:207px;top:30px"></span>
    <p class="env-web" style="top:82px">www.bellweatherpartners.example</p>
  </div>

  <div class="sheet envelope env-back-white">
    <svg width="475" height="144" viewBox="0 0 475 144">
      <polyline points="0,144 237,70 475,144" fill="none" stroke="var(--paper-shade)" stroke-width="1.5"/>
      <polyline points="0,25 237,66 475,25" fill="none" stroke="#dcdcdc" stroke-width="1.5"/>
    </svg>
    <span class="brand-mark flap-mark" style="left:225px;top:24px"></span>
    <p class="env-web" style="top:72px">www.bellweatherpartners.example</p>
  </div>

  <div class="sheet envelope env-front">
    <div class="brand"><span class="brand-mark"></span>BELLWEATHER</div>
    <p class="env-return">71 Pellham Lane, Marietta, Georgia 30008</p>
    <div class="sheet-footer">www.bellweatherpartners.example</div>
  </div>
  <p class="caption" style="left:679px;top:530px;width:480px">Envelope Design Back</p>

</body>
</html>
```